I need a business card design. I have a logo. Colors: black, white, orange, grey (i think)
In attachment there is design logo too (circle) but not sure do we need it on a business card (just same add info for your creativity)

```html
<!DOCTYPE html>
<html lang="en">
<head>
<meta charset="UTF-8">
<title>Velota – Business Card</title>
<link rel="stylesheet" href="https://fonts.googleapis.com/css2?family=Comfortaa:wght@400;600;700&family=Roboto:wght@400;500;700&display=swap">
<style>
  :root {
    --orange: #ec6a22;
    --orange-light: #f28a46;
    --grey: #8d8d8d;
    --grey-light: #b5b5b5;
    --charcoal: #3a3a3c;
    --ink: #333333;
    --paper: #ffffff;
    --backdrop: #d9d9d9;
  }
  * { margin: 0; padding: 0; box-sizing: border-box; }
  html, body {
    width: 1200px; height: 900px; overflow: hidden;
    background: var(--backdrop);
  }
  .stage { position: relative; width: 1200px; height: 900px; }

  .card {
    position: absolute;
    width: 560px; height: 320px;
    border-radius: 14px;
    overflow: hidden;
    box-shadow: 0 6px 18px rgba(0,0,0,.18);
  }
  .card__accent {
    position: absolute; left: 0; top: 0;
    width: 300px; height: 72px;
    background: linear-gradient(160deg, var(--orange-light) 0%, var(--orange) 55%, var(--grey) 100%);
  }

  /* Front */
  .card--front { left: 320px; top: 90px; background: var(--charcoal); }
  .wordmark {
    position: absolute; left: 0; right: 0; top: 140px;
    text-align: center;
    font-family: "Comfortaa", sans-serif; font-weight: 700;
    font-size: 52px; letter-spacing: 6px;
    color: var(--grey-light);
  }

  /* Back */
  .card--back { left: 320px; top: 490px; background: var(--paper); }
  .contact { position: absolute; left: 34px; top: 104px; }
  .contact__name {
    font-family: "Comfortaa", sans-serif; font-weight: 600;
    font-size: 24px; color: var(--ink);
  }
  .contact__name span { color: var(--orange); }
  .contact__role {
    font-family: "Roboto", sans-serif; font-weight: 700;
    font-size: 13px; color: var(--ink);
    margin: 4px 0 14px 112px;
  }
  .contact__list { list-style: none; font-family: "Roboto", sans-serif; font-size: 14px; color: var(--ink); }
  .contact__list li { display: flex; align-items: center; gap: 12px; height: 24px; }
  .contact__icon { width: 20px; height: 20px; flex: none; }
  .contact__text { line-height: 1.35; }
  .contact__list .spacer { width: 20px; flex: none; }

  .divider {
    position: absolute; left: 330px; top: 150px;
    width: 2px; height: 120px; background: var(--orange);
    transform: rotate(25deg);
  }
  .brand-mark {
    position: absolute; left: 372px; top: 150px;
    display: flex; align-items: center; gap: 10px;
  }
  .brand-mark__dot { width: 26px; height: 26px; border-radius: 50%; background: var(--orange); }
  .brand-mark__name {
    font-family: "Comfortaa", sans-serif; font-weight: 700;
    font-size: 28px; letter-spacing: 2px; color: var(--grey);
  }
</style>
</head>
<body>
<main class="stage">

  <section class="card card--front">
    <div class="card__accent" role="img" aria-label="Decorative corner accent in orange and grey"></div>
    <div class="wordmark">VELOTA</div>
  </section>

  <section class="card card--back">
    <div class="card__accent" role="img" aria-label="Decorative corner accent in orange and grey"></div>

    <div class="contact">
      <h1 class="contact__name">Andris <span>Kalnins</span></h1>
      <p class="contact__role">Rental manager</p>
      <ul class="contact__list">
        <li>
          <svg class="contact__icon" viewBox="0 0 20 20" aria-hidden="true">
            <circle cx="10" cy="10" r="10" fill="var(--orange)"/>
            <path d="M7 5.5 l2 2.2 -1 1.2 c.6 1.3 1.6 2.3 2.9 2.9 l1.2-1 2.2 2 -1.2 1.5 c-3.6-.4-6.7-3.5-7.1-7.1 z" fill="var(--paper)"/>
          </svg>
          <span class="contact__text">+506 8714 3092</span>
        </li>
        <li><span class="spacer"></span><span class="contact__text">+506 2241 7750 (office)</span></li>
        <li>
          <svg class="contact__icon" viewBox="0 0 20 20" aria-hidden="true">
            <circle cx="10" cy="10" r="10" fill="var(--orange)"/>
            <rect x="5" y="6.5" width="10" height="7" rx="1" fill="none" stroke="var(--paper)" stroke-width="1.3"/>
            <path d="M5.3 7 L10 10.5 L14.7 7" fill="none" stroke="var(--paper)" stroke-width="1.3"/>
          </svg>
          <span class="contact__text">hello@velota.com</span>
        </li>
        <li>
          <svg class="contact__icon" viewBox="0 0 20 20" aria-hidden="true">
            <circle cx="10" cy="10" r="10" fill="var(--orange)"/>
            <circle cx="10" cy="10" r="5" fill="none" stroke="var(--paper)" stroke-width="1.2"/>
            <ellipse cx="10" cy="10" rx="2.2" ry="5" fill="none" stroke="var(--paper)" stroke-width="1.1"/>
            <path d="M5 10 H15" stroke="var(--paper)" stroke-width="1.1"/>
          </svg>
          <span class="contact__text">www.velota.com</span>
        </li>
      </ul>
    </div>

    <div class="divider"></div>

    <div class="brand-mark">
      <span class="brand-mark__dot"></span>
      <span class="brand-mark__name">VELOTA</span>
    </div>
  </section>

</main>
</body>
</html>
```